Dential Clinic Business Card

We need a simple elegant business card. 2 sided. First side with our details, and 2nd side with appointment time rows.

Dark background preferred. Will consider monotone design, or colored. Surprise us.

Details:
SIDE1

Maplewood Square Dental

Dr Peter Hollis
BDSc(Adel) FRZPTA

Shop 42, Maplewood Square
7-19 Birch Parade, Ashbury Vale VIC 3188
Phone: 03 9555 0148
email: info@maplewoodsquaredental.com.au
site: www.maplewoodsquaredental.com.au
_____________________________________
SIDE 2
Appointed Time ________________________
Notes _______________________

Target Market(s)

Dental Patients

Industry/Entity Type

Healthcare

Contact Information for Business Card

SIDE1

Maplewood Square Dental

Dr Peter Hollis
Shop 42, Maplewood Square
Phone: 03 9555 0148
SIDE 2

Font styles to use
Other font styles liked:
• Comfortaa

Requirements
Must have
• Dr Peter Hollis
BDSc(Adel) FRZPTA

Address
Phone
Email
Website
Nice to have
• Simple elegant design with our logo.
Colored logo.
Light text on dark background - Side 1
Light background so can be written on with dark pen - SIde 2
Should not have
• Too many colors

```html
<!DOCTYPE html>
<html lang="en">
<head>
<meta charset="utf-8">
<title>Maplewood Square Dental – Business Card</title>
<link rel="stylesheet" href="https://fonts.googleapis.com/css2?family=Comfortaa:wght@400&family=Open+Sans:wght@400;600&family=Roboto+Slab:wght@700&display=swap">
<style>
  :root {
    --page-bg: #e9e6e2;
    --card-white: #ffffff;
    --green: #0a9a4a;
    --green-deep: #06803c;
    --green-dark: #1c3a1f;
    --green-name: #137a34;
    --brand-green: #5bb534;
    --ribbon-blue: #1c97d4;
    --ribbon-blue-dark: #1478ab;
    --ink: #5d5d5d;
    --rule: #9a9a9a;
  }
  * { box-sizing: border-box; margin: 0; padding: 0; }
  html, body { width: 1200px; height: 900px; overflow: hidden; }
  body {
    background: var(--page-bg);
    display: flex;
    align-items: center;
    justify-content: center;
    gap: 40px;
    font-family: "Open Sans", sans-serif;
  }
  .card {
    position: relative;
    width: 540px;
    height: 310px;
    border-radius: 22px;
    overflow: hidden;
    background: var(--card-white);
    box-shadow: 0 6px 18px rgba(0,0,0,.18);
  }
  .card svg.shapes { position: absolute; inset: 0; }

  /* brand */
  .brand {
    position: absolute;
    display: flex;
    align-items: center;
    gap: 12px;
  }
  .brand-dot {
    width: 34px; height: 34px;
    border-radius: 50%;
    background: var(--brand-green);
    flex: none;
  }
  .brand-name {
    font-family: "Comfortaa", sans-serif;
    font-weight: 400;
    font-size: 26px;
    color: var(--brand-green);
    white-space: nowrap;
  }
  .front .brand { left: 40px; top: 40px; }
  .back .brand { left: 34px; bottom: 44px; }

  /* front */
  .doctor-name {
    position: absolute;
    left: 34px; top: 117px;
    font-family: "Roboto Slab", serif;
    font-weight: 700;
    font-size: 16px;
    line-height: 22px;
    letter-spacing: 4px;
    color: #ffffff;
    text-transform: uppercase;
    white-space: nowrap;
  }
  .contact-icons {
    position: absolute;
    left: 150px; top: 159px;
    display: flex;
    gap: 14px;
  }
  .contact-icons svg { width: 24px; height: 24px; }
  .contact-list {
    position: absolute;
    left: 150px; top: 192px;
    list-style: none;
    color: #ffffff;
    font-size: 13.5px;
    line-height: 18px;
    white-space: nowrap;
  }

  /* back */
  .appointments {
    position: absolute;
    left: 36px; right: 36px; top: 30px;
  }
  .appointment-row {
    display: flex;
    align-items: baseline;
    gap: 8px;
    font-size: 11px;
    color: var(--ink);
    height: 28px;
  }
  .appointment-row .line {
    flex: 1;
    border-bottom: 1px solid var(--rule);
  }
  .appointment-row + .appointment-row.gap { margin-top: 14px; }
</style>
</head>
<body>

<section class="card front" aria-label="Card front">
  <svg class="shapes" width="540" height="310" viewBox="0 0 540 310">
    <polygon points="0,196 540,170 540,294 0,294" fill="var(--green)"/>
    <polygon points="0,240 540,230 540,294 0,294" fill="var(--green-deep)" opacity=".5"/>
    <polygon points="0,108 250,108 272,150 0,150" fill="var(--green-name)"/>
    <polygon points="118,156 372,156 390,184 135,184" fill="var(--ribbon-blue)"/>
    <polygon points="118,156 135,184 118,184" fill="var(--ribbon-blue-dark)"/>
  </svg>

  <div class="brand">
    <span class="brand-dot"></span>
    <span class="brand-name">Maplewood Square Dental</span>
  </div>

  <p class="doctor-name">Dr Peter Hollis</p>

  <div class="contact-icons">
    <svg viewBox="0 0 26 26" aria-label="Location"><circle cx="13" cy="13" r="11" fill="none" stroke="#fff" stroke-width="2"/><circle cx="13" cy="11" r="4" fill="none" stroke="#fff" stroke-width="2"/><path d="M10 15 L8 19" stroke="#fff" stroke-width="2"/></svg>
    <svg viewBox="0 0 26 26" aria-label="Website"><circle cx="13" cy="13" r="11" fill="none" stroke="#fff" stroke-width="2"/><path d="M13 7 L17 18 L13 15 L9 18 Z" fill="#fff"/></svg>
    <svg viewBox="0 0 26 26" aria-label="Email"><circle cx="13" cy="13" r="11" fill="none" stroke="#fff" stroke-width="2"/><rect x="8" y="9" width="10" height="8" fill="none" stroke="#fff" stroke-width="1.6"/><path d="M8 9 L13 14 L18 9" fill="none" stroke="#fff" stroke-width="1.6"/></svg>
    <svg viewBox="0 0 26 26" aria-label="Phone"><circle cx="13" cy="13" r="11" fill="none" stroke="#fff" stroke-width="2"/><path d="M10 8 Q8 13 13 18 L15 16 L13 14 Q11 12 12 10 Z" fill="#fff"/></svg>
  </div>

  <ul class="contact-list">
    <li>03 9555 0148</li>
    <li>info@maplewoodsquaredental.com.au</li>
    <li>www.maplewoodsquaredental.com.au</li>
    <li>Shop 42, Maplewood Square</li>
    <li>7-19 Birch Parade, Ashbury Vale VIC 3188</li>
  </ul>
</section>

<section class="card back" aria-label="Card back">
  <svg class="shapes" width="540" height="310" viewBox="0 0 540 310">
    <rect x="0" y="200" width="540" height="110" fill="var(--green-dark)"/>
  </svg>

  <div class="appointments">
    <div class="appointment-row"><span>Appointed Time</span><span class="line"></span></div>
    <div class="appointment-row"><span>Notes</span><span class="line"></span></div>
    <div class="appointment-row gap"><span>Appointed Time</span><span class="line"></span></div>
    <div class="appointment-row"><span>Notes</span><span class="line"></span></div>
  </div>

  <div class="brand">
    <span class="brand-dot"></span>
    <span class="brand-name">Maplewood Square Dental</span>
  </div>
</section>

</body>
</html>
```